Brightwater Communications

I need a very clean, uncomplicated design for an LA-based, very senior level strategic communications firm with about four associates. Landing page should stress LA, maybe a slider with downtown skyline, Corvana pier, and Tamsen Drive. In addition to landing page with firm's description, all else we'd need is services offered page and another for bios of associates.

Industry/Entity Type

Communications

Font styles to use
Sans Serif

```html
<!DOCTYPE html>
<html lang="en">
<head>
<meta charset="utf-8">
<title>Brightwater Communications</title>
<link rel="stylesheet" href="https://fonts.googleapis.com/css2?family=Jost:wght@300;400;500;600&display=swap">
<style>
  :root {
    --blue: #0b6aa7;
    --blue-light: #1a8fd6;
    --navy: #183f5c;
    --dark: #333333;
    --panel: #f2f2f2;
    --ink: #222222;
    --muted: #444444;
    --white: #ffffff;
  }
  * { box-sizing: border-box; margin: 0; padding: 0; }
  html, body { width: 1200px; height: 2359px; overflow: hidden; }
  body { position: relative; font-family: "Jost", Arial, sans-serif; color: var(--ink); background: var(--white); }
  .abs { position: absolute; }

  /* Hero */
  .hero { position: absolute; left: 0; top: 0; width: 1200px; height: 712px;
    background: linear-gradient(180deg, #1f5ed8 0%, #3f74d8 30%, #5b6bb8 45%, #c46a6a 55%, #8a5a3a 65%, #3b3a44 80%, #5a4030 100%); }
  .header { position: absolute; left: 171px; top: 0; width: 856px; height: 90px; background: linear-gradient(#ffffff, #ececec);
    box-shadow: 0 6px 10px rgba(0,0,0,.35); }
  .brand { position: absolute; left: 14px; top: 24px; display: flex; align-items: center; gap: 10px; }
  .brand-mark { width: 46px; height: 46px; border-radius: 50%; background: var(--blue); }
  .brand-name { font-size: 22px; line-height: 20px; font-weight: 500; color: var(--navy); }
  .nav { position: absolute; right: 36px; top: 32px; display: flex; gap: 28px; font-size: 16px; color: var(--ink); }
  .tagline { position: absolute; top: 133px; width: 1200px; text-align: center; color: var(--white); font-size: 26px; font-weight: 300; }
  .slide-arrow { position: absolute; top: 302px; width: 61px; height: 80px; background: rgba(25,35,60,.85); }
  .slide-arrow svg { position: absolute; left: 20px; top: 28px; }
  .service { position: absolute; top: 527px; height: 185px; background: var(--blue); border-top: 7px solid var(--blue-light); color: var(--white); padding: 18px 15px 0; }
  .service h2 { font-size: 25px; font-weight: 400; line-height: 30px; }
  .service p { margin-top: 14px; font-size: 11.5px; line-height: 20px; padding-left: 5px; }

  /* About */
  .about { position: absolute; left: 0; top: 712px; width: 1200px; height: 353px; background: var(--dark); color: var(--white); }
  .about h2 { position: absolute; left: 190px; top: 62px; font-size: 26px; font-weight: 400; }
  .about-text { position: absolute; left: 190px; top: 112px; width: 480px; font-size: 11.2px; line-height: 20.5px; }
  .about-text p + p { margin-top: 20px; }
  .newsletter { position: absolute; left: 738px; top: 43px; width: 273px; height: 268px; background: var(--panel); color: var(--ink);
    box-shadow: 0 4px 10px rgba(0,0,0,.5); padding: 12px 13px; }
  .newsletter h3 { font-size: 25px; font-weight: 400; line-height: 31px; color: var(--blue); }
  .newsletter p { font-size: 11.5px; line-height: 20px; margin-top: 8px; }
  .field { height: 33px; border: 1px solid #d4d4d4; background: var(--white); margin-top: 8px; font-size: 11px; color: #bbb; padding: 9px 8px; }
  .field:first-of-type { margin-top: 10px; }
  .subscribe { display: inline-block; margin-top: 11px; background: var(--blue); color: var(--white); font-size: 12px; font-weight: 500; padding: 8px 20px; }

  /* News */
  .section-title { position: absolute; width: 1200px; text-align: center; font-size: 26px; font-weight: 400; color: var(--ink); }
  .news-card { position: absolute; top: 1169px; width: 260px; height: 188px; background: var(--blue); color: var(--white); padding: 18px 17px; }
  .news-card.current { background: var(--navy); }
  .news-card h4 { font-size: 15px; font-weight: 600; }
  .news-card .go { position: absolute; right: 16px; top: 17px; }
  .news-card p { font-size: 16px; line-height: 20.5px; margin-top: 5px; }
  .news-card time { position: absolute; left: 17px; top: 150px; font-size: 16px; }

  /* Articles */
  .article { position: absolute; top: 1477px; width: 260px; height: 343px; background: var(--panel); }
  .article-photo { height: 153px; }
  .article h4 { padding: 20px 13px 0; font-size: 15.5px; line-height: 24px; font-weight: 500; color: var(--blue); }
  .article p { padding: 10px 13px 0; font-size: 11.2px; line-height: 20px; text-align: justify; color: var(--muted); }

  /* Testimonials */
  .testimonials { position: absolute; left: 0; top: 1865px; width: 1200px; height: 334px; background: var(--blue); color: var(--white); text-align: center; }
  .testimonials h2 { margin-top: 17px; font-size: 26px; font-weight: 400; }
  .quote-mark { position: absolute; left: 189px; top: 52px; }
  .quote { position: absolute; left: 180px; top: 92px; width: 840px; font-size: 21px; line-height: 31px; font-weight: 300; }
  .author { position: absolute; top: 215px; width: 1200px; font-size: 20px; font-weight: 600; }
  .city { position: absolute; top: 243px; width: 1200px; font-size: 16px; }
  .dots { position: absolute; left: 552px; top: 290px; display: flex; gap: 7px; }
  .dots span { width: 19px; height: 19px; border-radius: 50%; background: #000; }
  .dots span.active { background: var(--blue-light); }

  /* Footer */
  .footer { position: absolute; left: 0; top: 2199px; width: 1200px; height: 160px; background: var(--dark); color: var(--white); text-align: center; }
  .social { position: absolute; left: 514px; top: 34px; display: flex; gap: 3px; }
  .social span { width: 32px; height: 32px; border-radius: 50%; border: 2px solid var(--white); }
  .footer-nav { position: absolute; top: 88px; width: 1200px; font-size: 13px; }
  .footer-nav span { padding: 0 14px; }
  .copyright { position: absolute; top: 117px; width: 1200px; font-size: 13px; }
</style>
</head>
<body>

<section class="hero" role="img" aria-label="Downtown Los Angeles skyline at dusk">
</section>

<header class="header">
  <div class="brand">
    <span class="brand-mark"></span>
    <span class="brand-name">brightwater<br>communications</span>
  </div>
  <nav class="nav">
    <span>Home</span><span>About us</span><span>Services</span><span>Associates</span><span>Contact us</span>
  </nav>
</header>

<h1 class="tagline">We are a senior level strategic communications firm</h1>

<div class="slide-arrow" style="left:0">
  <svg width="20" height="24" viewBox="0 0 20 24"><path d="M14 2 L4 12 L14 22" fill="none" stroke="#fff" stroke-width="4"/></svg>
</div>
<div class="slide-arrow" style="left:1139px">
  <svg width="20" height="24" viewBox="0 0 20 24"><path d="M6 2 L16 12 L6 22" fill="none" stroke="#fff" stroke-width="4"/></svg>
</div>

<article class="service" style="left:190px;width:280px">
  <h2>Corporate<br>Communications »</h2>
  <p>Lorem Ipsum is simply dummy text of the printing and typesetting industry. Lorem Ipsum has been the industry's</p>
</article>
<article class="service" style="left:472px;width:273px;background:linear-gradient(90deg,#0a5a8f,#0b6aa7 10%)">
  <h2>Financial<br>Communications »</h2>
  <p>Lorem Ipsum is simply dummy text of the printing and typesetting industry. Lorem Ipsum has been the industry's</p>
</article>
<article class="service" style="left:745px;width:266px;background:linear-gradient(90deg,#0a5a8f,#0b6aa7 10%)">
  <h2>Digital<br>Communications »</h2>
  <p>Lorem Ipsum is simply dummy text of the printing and typesetting industry. Lorem Ipsum has been the industry's</p>
</article>

<section class="about">
  <h2>About Us</h2>
  <div class="about-text">
    <p>Lorem Ipsum is simply dummy text of the printing and typesetting industry. Lorem Ipsum has been the industry's standard dummy text ever since the 1500s, when an unknown printer took a galley of type and scrambled it to make a type specimen book. It has survived not only five centuries, but also the leap into electronic typesetting, remaining essentially unchanged. Lorem Ipsum is simply dummy text of the printing and typesetting industry.</p>
    <p>Lorem Ipsum has been the industry's standard dummy text ever since the 1500s, when an unknown printer took a galley of type and scrambled it to make a type specimen book. It has survived not only five centuries, but also the leap into electronic typesetting, remaining essentially unchanged.</p>
  </div>
  <aside class="newsletter">
    <h3>Newsletter<br>Sign-Up</h3>
    <p>Lorem Ipsum has been the industry's standard dummy text ever since the 1500s</p>
    <div class="field">Name</div>
    <div class="field">E-Mail</div>
    <span class="subscribe">SUBSCRIBE</span>
  </aside>
</section>

<h2 class="section-title" style="top:1100px">NEWS</h2>

<article class="news-card current" style="left:190px">
  <h4>Communications</h4>
  <svg class="go" width="18" height="18" viewBox="0 0 18 18"><circle cx="9" cy="9" r="9" fill="#fff"/><path d="M7 5 L11 9 L7 13" fill="none" stroke="#183f5c" stroke-width="2.2"/></svg>
  <p>Lorem Ipsum has been the industry's standard dummy text ever since the 1500s, when an unknown printer took</p>
  <time>07/09/2014</time>
</article>
<article class="news-card" style="left:472px">
  <h4>Communications</h4>
  <svg class="go" width="18" height="18" viewBox="0 0 18 18"><circle cx="9" cy="9" r="9" fill="#fff"/><path d="M7 5 L11 9 L7 13" fill="none" stroke="#0b6aa7" stroke-width="2.2"/></svg>
  <p>Lorem Ipsum has been the industry's standard dummy text ever since the 1500s, when an unknown printer took</p>
  <time>07/09/2014</time>
</article>
<article class="news-card" style="left:752px">
  <h4>Communications</h4>
  <svg class="go" width="18" height="18" viewBox="0 0 18 18"><circle cx="9" cy="9" r="9" fill="#fff"/><path d="M7 5 L11 9 L7 13" fill="none" stroke="#0b6aa7" stroke-width="2.2"/></svg>
  <p>Lorem Ipsum has been the industry's standard dummy text ever since the 1500s, when an unknown printer took</p>
  <time>07/09/2014</time>
</article>

<h2 class="section-title" style="top:1421px">FEATURED ARTICLES</h2>
<svg class="abs" style="left:189px;top:1429px" width="14" height="22" viewBox="0 0 14 22"><path d="M11 2 L3 11 L11 20" fill="none" stroke="#999" stroke-width="3"/></svg>
<svg class="abs" style="left:997px;top:1429px" width="14" height="22" viewBox="0 0 14 22"><path d="M3 2 L11 11 L3 20" fill="none" stroke="#999" stroke-width="3"/></svg>

<article class="article" style="left:190px">
  <div class="article-photo" role="img" aria-label="Team collaborating around a table" style="background:linear-gradient(135deg,#d8d2c8,#c89a80 50%,#e6e4e0)"></div>
  <h4>Lorem Ipsum is simply dummy text of the printing and typesetting</h4>
  <p>Lorem Ipsum has been the industry's standard dummy text ever since the 1500s, when an unknown printer took a galley of type and scrambled it to make a type specimen book.</p>
</article>
<article class="article" style="left:472px">
  <div class="article-photo" role="img" aria-label="Business person touching a digital screen" style="background:linear-gradient(135deg,#8aa0b8,#b8c4d0 50%,#6a7e96)"></div>
  <h4>Lorem Ipsum is simply dummy text of the printing and typesetting</h4>
  <p>Lorem Ipsum has been the industry's standard dummy text ever since the 1500s, when an unknown printer took a galley of type and scrambled it to make a type specimen book.</p>
</article>
<article class="article" style="left:752px">
  <div class="article-photo" role="img" aria-label="Business people silhouetted against office windows" style="background:linear-gradient(180deg,#3a3a3a,#d6d6d6 40%,#ededed 70%,#222 100%)"></div>
  <h4>Lorem Ipsum is simply dummy text of the printing and typesetting</h4>
  <p>Lorem Ipsum has been the industry's standard dummy text ever since the 1500s, when an unknown printer took a galley of type and scrambled it to make a type specimen book.</p>
</article>

<section class="testimonials">
  <h2>TESTIMONIALS</h2>
  <svg class="quote-mark" width="40" height="30" viewBox="0 0 40 30"><g fill="#fff"><circle cx="9" cy="20" r="8"/><path d="M2 20 C2 8 8 3 15 1 L16 4 C11 6 8 10 8 16 Z"/><circle cx="30" cy="20" r="8"/><path d="M23 20 C23 8 29 3 36 1 L37 4 C32 6 29 10 29 16 Z"/></g></svg>
  <p class="quote">Lorem Ipsum is simply dummy text of the printing and typesetting industry. Lorem Ipsum has been the industry's standard dummy text ever since the 1500s, when an unknown printer took a galley of type and scrambled</p>
  <p class="author">Daniel Harrow</p>
  <p class="city">LONDON</p>
  <div class="dots"><span class="active"></span><span></span><span></span><span></span></div>
</section>

<footer class="footer">
  <div class="social"><span></span><span></span><span></span><span></span><span></span></div>
  <div class="footer-nav"><span>Home</span>|<span>About Us</span>|<span>Services</span>|<span>Associates</span>|<span>Contact us</span></div>
  <p class="copyright">© 2014 Company Name ,All Rights Reserved</p>
</footer>

</body>
</html>
```